Corvalith business website

I am wanting a website for my media agency Corvalith.

It needs to be be an attractive, unique and professional looking website. The website is a destination for people to be able to understand the service that Corvalith offers.

Please read uploaded website copy to gain an understanding of the business.

Target Market(s)

small business owners, business decision makers, marketing managers,

Industry/Entity Type

Business

Requirements
Must have
• Good branding.

```html
<!DOCTYPE html>
<html lang="en">
<head>
<meta charset="utf-8">
<title>Corvalith — media agency</title>
<link rel="stylesheet" href="https://fonts.googleapis.com/css2?family=PT+Sans:wght@400;700&family=Arimo:wght@400&display=swap">
<style>
:root{
  --brand-blue:#0000dd;
  --brand-violet:#5a48ee;
  --hero-red-top:#ff6363;
  --hero-red-bottom:#f23a3e;
  --cta-orange:#ff7b00;
  --panel-grey:#dedede;
  --people-grey:#9a9a9a;
  --text-dark:#444;
  --text-mid:#666;
  --white:#fff;
}
*{box-sizing:border-box;margin:0;padding:0}
html,body{width:928px;height:1200px;overflow:hidden;background:var(--white)}
body{position:relative;font-family:"PT Sans",sans-serif;color:var(--text-dark)}
.abs{position:absolute}

/* header */
.brand{left:87px;top:40px;display:flex;align-items:center;gap:8px;font-family:"PT Sans",sans-serif;font-size:26px;font-weight:700;color:var(--brand-blue);white-space:nowrap}
.brand-mark{width:22px;height:22px;background:var(--brand-violet);display:block}
.social{left:332px;top:42px;display:flex;gap:7px}
.social span{width:24px;height:24px;display:block}
.social .s1{background:#0000cc}.social .s2{background:#2aa3e6}.social .s3{background:#d8463a}
.search{left:684px;top:42px;width:162px;height:23px;border:1px solid #999;box-shadow:inset 1px 1px 2px #bbb;font-family:"Arimo",sans-serif;font-style:italic;font-size:10px;color:#555;padding:5px 0 0 30px}
.search svg{position:absolute;left:7px;top:3px}
.nav{top:106px;left:331px;height:20px;font-family:"Arimo",sans-serif;font-size:16px;color:#333}
.nav a{position:absolute;top:1px;white-space:nowrap;color:inherit;text-decoration:none}
.nav .active{background:var(--brand-blue);color:var(--white);padding:0 8px;top:0;height:20px;line-height:21px}
.nav i{position:absolute;top:4px;height:13px;border-left:1px dotted #77a}

/* hero */
.hero{left:0;top:135px;width:928px;height:241px;overflow:hidden;background:var(--hero-red-top)}
.hero svg{position:absolute;left:0;top:0}
.hero h1{position:absolute;left:78px;top:17px;font-size:24px;line-height:29px;font-weight:700;color:var(--white);white-space:nowrap}
.btn-more{position:absolute;left:80px;top:89px;width:103px;height:31px;background:var(--cta-orange);color:var(--white);font-size:20px;text-align:center;line-height:31px;border-radius:2px}
.hero-photo{position:absolute;left:548px;top:3px;width:180px;height:238px;background:linear-gradient(#c9a58a 0 18%,#252a36 30%,#1d2130);border-radius:60px 60px 10px 10px}

/* services */
.tab{top:376px;height:96px;font-size:21px;line-height:26px;text-align:center;color:var(--text-mid)}
.tab-left{left:100px;width:200px;top:401px}
.tab-right{left:684px;top:401px;text-align:left}
.tab-active{left:344px;width:223px;background:var(--brand-blue);color:var(--white);padding-top:23px}
.panel{left:80px;top:472px;width:768px;height:225px;background:var(--panel-grey)}
.pointer{left:440px;top:472px}
.points{left:90px;top:510px;width:680px;list-style:none;font-size:15.4px;line-height:19.2px;color:#555}
.points li{position:relative;padding-left:23px;margin-bottom:38px}
.points li::before{content:"";position:absolute;left:2px;top:8px;width:7px;height:7px;border-radius:50%;background:var(--brand-violet)}
.btn-learn{left:607px;top:644px;width:145px;height:32px;background:var(--brand-violet);color:var(--white);font-family:"Arimo",sans-serif;font-size:20px;text-align:center;line-height:32px;border-radius:2px}

/* people */
.people-bg{left:0;top:718px}
.people-title{left:0;width:924px;top:748px;text-align:center;color:var(--white);font-size:31px;font-weight:700}
.people-copy{left:78px;top:827px;width:600px;font-size:15.4px;line-height:19.2px;color:var(--white);white-space:nowrap}
.people-copy p+p{margin-top:19.2px}
.portrait{left:676px;top:826px;width:128px;height:134px;background:linear-gradient(#8a8a8a,#7f7f7f);border-radius:40px 40px 4px 4px}

/* footer */
.footer-nav{left:0;width:924px;top:1093px;display:flex;justify-content:center;font-size:10px;color:#333}
.footer-nav span{padding:0 9px;border-left:2px solid var(--brand-blue);line-height:12px}
.footer-nav span:first-child{border-left:0}
.copyright{left:0;width:924px;top:1121px;text-align:center;font-size:10px;color:#333}
.footer-brand{left:758px;top:1098px;display:flex;align-items:center;gap:5px;font-size:16px;font-weight:700;color:var(--brand-blue);white-space:nowrap}
.footer-brand .brand-mark{width:14px;height:14px}
</style>
</head>
<body>

<header>
  <div class="abs brand"><span class="brand-mark"></span>Corvalith</div>
  <div class="abs social" aria-label="Social links"><span class="s1"></span><span class="s2"></span><span class="s3"></span></div>
  <div class="abs search">
    <svg width="18" height="18" viewBox="0 0 18 18"><circle cx="10" cy="7" r="5" fill="none" stroke="#666" stroke-width="1.5"/><line x1="6.5" y1="10.5" x2="2" y2="15" stroke="#666" stroke-width="2"/></svg>
    Search here...
  </div>
  <nav class="abs nav">
    <a style="left:0">HOME</a><i style="left:58px"></i>
    <a style="left:71px">ABOUT</a><i style="left:136px"></i>
    <a style="left:150px">WHAT WE DO</a><i style="left:263px"></i>
    <a class="active" style="left:272px">PEOPLE</a><i style="left:352px"></i>
    <a style="left:369px">IDEAS</a><i style="left:431px"></i>
    <a style="left:447px">CONTACT</a>
  </nav>
</header>

<section class="abs hero">
  <svg width="928" height="241" viewBox="0 0 928 241">
    <defs><linearGradient id="heroLow" x1="0" y1="0" x2="0" y2="1"><stop offset="0" stop-color="#f5484b"/><stop offset="1" stop-color="var(--hero-red-bottom)"/></linearGradient></defs>
    <path d="M0 145 Q464 60 928 150 L928 241 L0 241Z" fill="url(#heroLow)"/>
  </svg>
  <h1>Corvalith is media strategy planning<br>and buying agency</h1>
  <div class="btn-more">MORE</div>
  <div class="hero-photo" role="img" aria-label="Photo of a smiling businessman in a dark suit holding a phone and an open folder"></div>
</section>

<section>
  <div class="abs tab tab-left">Media Strategy,<br>Planning</div>
  <div class="abs tab tab-active">Media Trading ,<br>Campaign Monitoring</div>
  <div class="abs tab tab-right">Content,<br>Creative</div>
  <div class="abs panel"></div>
  <svg class="abs pointer" width="32" height="29" viewBox="0 0 32 29"><path d="M0 0H32L16 29Z" fill="var(--brand-blue)"/></svg>
  <ul class="abs points">
    <li>Using our media partner relationships, trade negotiation techniques &amp; experience we achieve a high level of value for all media buys that leads to significant cost savings for clients.</li>
    <li>All media activity is monitored &amp; optimized to ensure performance.</li>
  </ul>
  <div class="abs btn-learn">LEARN MORE</div>
</section>

<section>
  <svg class="abs people-bg" width="928" height="442" viewBox="0 0 928 442">
    <defs><linearGradient id="footBand" x1="0" y1="0" x2="0" y2="1"><stop offset="0" stop-color="#fff"/><stop offset="0.6" stop-color="#f6f6f6"/><stop offset="1" stop-color="#d9d9d9"/></linearGradient></defs>
    <path d="M80 0H848L928 94V346L848 440H80L0 346V94Z" fill="var(--people-grey)"/>
    <path d="M0 346H928V360L848 440H80L0 360Z" fill="#bdbdbd"/>
    <path d="M14 360H914L844 436H84Z" fill="url(#footBand)"/>
  </svg>
  <h2 class="abs people-title">People</h2>
  <div class="abs people-copy">
    <p>Corvalith is led by Media Director Martin Dalby.<br>Martin has worked in media many years on both sides of the trade<br>fence for leading media outlets and global media planning &amp; buying agencies<br>working across all forms of media.</p>
    <p>Martin, along with our media partners have lots of experience &amp; know<br>how to get the best out of the media so our clients get great results.</p>
  </div>
  <div class="abs portrait" role="img" aria-label="Faded silhouette of a man in a suit"></div>
</section>

<footer>
  <div class="abs footer-nav"><span>HOME</span><span>ABOUT</span><span>WHAT WE DO</span><span>PEOPLE</span><span>IDEAS</span><span>CONTACT</span></div>
  <div class="abs copyright">Copyrights @ 2013 All Rights Reserved</div>
  <div class="abs footer-brand"><span class="brand-mark"></span>Corvalith</div>
</footer>

</body>
</html>
```